Kestrel Dawn Magazine need Logo desing and front page for 1 edittion

This is a new magazine that will be circulating in Panama. the magazine will run non for profit,will be mostly informative and few advertizers to cover printing costs.
the magaine will oncce every 2 or 3 month. we need to present it to the editors who will be aproving or diss aproving the project.

we need a Logo desing for the name of the magazine "Kestrel Dawn" and the "front cover desing for the first edition" it will be good if the designer can incude the designed format for the iner magazine, for us just to add in the artucles and the spaces for advertizing.

the magazine content will be articles by govenment energy sectors, gloval warming articles, articles in renewvable enery, university profesor talking or promoting new ideas or university advances, orientations, special edition on book or international articles about the subject on saving enerty, different sectors, world innovations in renewbable energy, and the companies who will advertize will be comapnies selling VRAX products, companies offfering product and services on renewvable energy, Led product and systems companies etc...

```html
<!DOCTYPE html>
<html lang="en">
<head>
<meta charset="utf-8">
<title>Kestrel Dawn Magazine – Cover and Inner Spread</title>
<link rel="stylesheet" href="https://fonts.googleapis.com/css2?family=Open+Sans:wght@400;600;700&family=Oswald:wght@500&display=swap">
<style>
  :root {
    --bg: #e9e9ea;
    --paper: #ffffff;
    --brand-blue: #2b6fb6;
    --brand-green: #7dbb2e;
    --purple: #5b4396;
    --sub-blue: #4a5db0;
    --ink: #4a4a4a;
    --ink-soft: #777777;
    --dark: #3a3a3a;
    --tab: #4b4b4b;
    --sky: #6fa6dc;
    --panel: #2c3f78;
    --leaf: #5f8f3a;
  }
  * { box-sizing: border-box; margin: 0; padding: 0; }
  html, body { width: 1200px; height: 886px; overflow: hidden; }
  body {
    background: var(--bg);
    font-family: "Open Sans", Arial, sans-serif;
    color: var(--ink);
    position: relative;
  }
  .page {
    position: absolute;
    background: var(--paper);
    box-shadow: 0 6px 18px rgba(0,0,0,.18);
    overflow: hidden;
  }

  /* ---------- Cover ---------- */
  .cover { left: 30px; top: 200px; width: 360px; height: 480px; }
  .masthead {
    position: absolute; left: 20px; top: 16px;
    display: flex; align-items: center; gap: 8px;
  }
  .masthead-dot { width: 14px; height: 14px; border-radius: 50%; background: var(--brand-green); }
  .masthead-name {
    font-weight: 600; font-size: 38px; line-height: 1;
    color: var(--brand-blue); letter-spacing: -0.5px;
  }
  .issue-line {
    position: absolute; right: 22px; top: 62px;
    font-size: 8px; font-weight: 600; color: var(--brand-blue);
  }
  .cover-art { position: absolute; left: 0; top: 70px; width: 360px; height: 300px; }
  .cover-copy { position: absolute; left: 22px; top: 376px; width: 320px; }
  .cover-headline {
    font-size: 14px; font-weight: 700; line-height: 16px;
    color: var(--purple); text-transform: uppercase;
  }
  .cover-feature { font-size: 17px; color: var(--dark); line-height: 22px; margin-top: 4px; }
  .cover-url { font-size: 11px; font-weight: 700; color: var(--brand-green); margin-top: 2px; }
  .cover-footer {
    position: absolute; left: 0; bottom: 0; width: 100%; height: 22px;
    background: var(--dark); color: #fff;
    font-size: 8px; font-weight: 600; letter-spacing: .4px;
    padding: 6px 22px; text-transform: uppercase;
  }

  /* ---------- Spread ---------- */
  .spread-left { left: 410px; top: 190px; width: 380px; height: 506px; }
  .spread-right { left: 790px; top: 190px; width: 380px; height: 506px; }
  .gutter {
    position: absolute; left: 770px; top: 190px; width: 40px; height: 506px;
    background: linear-gradient(90deg, rgba(0,0,0,0) 0%, rgba(0,0,0,.10) 50%, rgba(0,0,0,0) 100%);
  }
  .page-rule { position: absolute; height: 5px; background: var(--brand-green); }
  .page-tab {
    position: absolute; width: 42px; height: 22px; background: var(--tab);
    color: #fff; font-weight: 700; font-size: 12px; line-height: 22px; text-align: center;
  }
  .article-visual {
    position: absolute; left: 132px; top: 56px; width: 116px; height: 150px;
    border-radius: 58px 58px 20px 20px;
    background: linear-gradient(180deg, #8fc3e4 0%, #cde6b8 60%, #9a9a9a 100%);
  }
  .article-title {
    position: absolute; left: 30px; top: 208px; width: 330px;
    font-size: 25px; font-weight: 700; line-height: 29px; color: var(--brand-blue);
  }
  .article-sub {
    position: absolute; left: 30px; top: 270px; width: 330px;
    font-size: 9.5px; font-weight: 700; color: var(--sub-blue); text-transform: uppercase;
  }
  .article-intro {
    position: absolute; left: 30px; top: 288px; width: 160px;
    font-size: 6px; line-height: 8px; font-weight: 600; color: var(--brand-green); text-transform: uppercase;
  }
  .body-text {
    position: absolute; font-size: 6.2px; line-height: 8.2px; color: var(--ink-soft);
    text-align: justify;
  }
  .pull-quote-green {
    position: absolute; left: 200px; top: 22px; width: 160px;
    font-size: 6px; line-height: 8px; font-weight: 600; color: var(--brand-green); text-transform: uppercase;
  }
  .spread-art { position: absolute; left: 0; top: 90px; width: 380px; height: 190px; }
  .hex-quote {
    position: absolute; left: 222px; top: 142px; width: 140px;
    font-family: "Oswald", "Arial Narrow", sans-serif; font-weight: 500;
    font-size: 8px; line-height: 10px; letter-spacing: .6px; color: #fff;
    text-align: center; text-transform: uppercase;
  }
  .bottom-band { position: absolute; left: 0; top: 430px; width: 380px; height: 40px; }
</style>
</head>
<body>

  <!-- Cover -->
  <section class="page cover">
    <div class="masthead">
      <span class="masthead-name">Kestrel Dawn</span>
      <span class="masthead-dot"></span>
    </div>
    <div class="issue-line">ISSUE 12, FEBRUARY 2014</div>

    <svg class="cover-art" viewBox="0 0 360 300">
      <defs>
        <linearGradient id="panelTone" x1="0" y1="0" x2="0" y2="1">
          <stop offset="0" stop-color="#8fbbe6"/>
          <stop offset="1" stop-color="#24366d"/>
        </linearGradient>
        <linearGradient id="treeTone" x1="0" y1="0" x2="0" y2="1">
          <stop offset="0" stop-color="#9cc4ea"/>
          <stop offset=".45" stop-color="#6e9d45"/>
          <stop offset="1" stop-color="#2f4f7a"/>
        </linearGradient>
      </defs>
      <polygon role="img" aria-label="Photo of solar panels" fill="url(#panelTone)"
        points="307,235 276,181.3 214,181.3 183,235 214,288.7 276,288.7"/>
      <polygon role="img" aria-label="Photo of rows of solar panels under blue sky" fill="url(#panelTone)"
        points="350,70 302.5,-12.3 207.5,-12.3 160,70 207.5,152.3 302.5,152.3"/>
      <polygon role="img" aria-label="Photo of green trees in sunlight beside solar panels" fill="url(#treeTone)"
        points="230,180 182.5,97.7 87.5,97.7 40,180 87.5,262.3 182.5,262.3"/>
    </svg>

    <div class="cover-copy">
      <p class="cover-headline">Sustainable building<br>for sustainable living</p>
      <p class="cover-feature">Sun Energy &amp; Photovoltaics</p>
      <p class="cover-url">www.kestreldawn.example</p>
    </div>
    <div class="cover-footer">Read more: international energy news</div>
  </section>

  <!-- Inner spread, left page -->
  <section class="page spread-left">
    <div class="page-rule" style="left:50px; top:38px; width:330px;"></div>
    <div class="page-tab" style="left:20px; top:30px;">4</div>
    <div class="article-visual" role="img" aria-label="Illustration of a light bulb holding a small tree"></div>
    <h1 class="article-title">Main Headline And Title Here For Article</h1>
    <p class="article-sub">Insert subheader here insert subheader here</p>
    <p class="article-intro">Lorem ipsum nulla sed convallis orci, curabitur mattis nibh id nisi hendrerit fermentum. Donec sit amet leo nec justo lobortis tempor at sit amet dui.</p>
    <p class="body-text" style="left:30px; top:322px; width:158px;">Donec ut lorem sed ligula tempus sagittis. Mauris vel cursus massa. Maecenas et massa nec metus vestibulum malesuada id eget odio. Ut erat nibh, vestibulum id magna vel, ullamcorper bibendum tellus. Sed eleifend tempor lorem eget consectetur. Cum sociis natoque penatibus et magnis dis parturient montes, nascetur ridiculus mus. Vivamus tristique eros mauris, nec sodales ante sollicitudin id. Ut in fermentum nisl. Nulla venenatis, metus egestas iaculis dapibus, enim nisi egestas justo, viverra venenatis lorem lacus dictum nisl.</p>
    <p class="body-text" style="left:202px; top:300px; width:158px;">Suspendisse luctus massa vel, in neque aliquam at. Nulla sed venenatis. Nullam molestie consectetur dolor et convallis. Nam rutrum consequat dolor, sed consectetur nisi egestas tincidunt nec. Morbi blandit sapien at enim tempus, eget vehicula mi gravida. Donec id ultricies ante, vel ornare tellus. In justo erat, gravida at nibh et, fermentum id mi. Suspendisse potenti. Aenean vel lorem consequat venenatis. Maecenas eu euismod turpis. Ut orci dui, elementum fringilla nec, vulputate sed mauris. Proin sollicitudin sit amet viverra lobortis. Aenean orci nisi, bibendum at bibendum faucibus, fermentum ac tellus. Aliquet a risus non, tristique viverra tortor.</p>
  </section>

  <!-- Inner spread, right page -->
  <section class="page spread-right">
    <p class="body-text" style="left:20px; top:22px; width:165px;">Curabitur vehicula lorem sem et nisi gravida euismod. Cras vitae accumsan ligula, eu velit dapibus eu. Nulla tincidunt auctor magna, in laoreet neque hendrerit eu. Cras malesuada nunc id faucibus mi. Curabitur commodo urna eu egestas ante fermentum. Phasellus aliquet turpis.</p>
    <p class="pull-quote-green">Sed gravida mollis a iaculis nec, bibendum vel felis. Pellentesque dictum nisl sed augue gravida molestie, sed pharetra tortor ac scelerisque hendrerit etiam vel neque elit.</p>

    <svg class="spread-art" viewBox="0 0 380 190">
      <defs>
        <linearGradient id="windTone" x1="0" y1="0" x2="0" y2="1">
          <stop offset="0" stop-color="#3f7fcf"/>
          <stop offset="1" stop-color="#c9def2"/>
        </linearGradient>
        <linearGradient id="spreadPanelTone" x1="0" y1="0" x2="0" y2="1">
          <stop offset="0" stop-color="#bcd6ef"/>
          <stop offset=".45" stop-color="#3a5596"/>
          <stop offset="1" stop-color="#1f2f62"/>
        </linearGradient>
      </defs>
      <path d="M0 22 C 120 6, 250 10, 380 26" fill="none" stroke="var(--brand-green)" stroke-width="3"/>
      <polygon role="img" aria-label="Photo of wind turbines under blue sky" fill="url(#windTone)"
        points="135,95 107.5,47.4 52.5,47.4 25,95 52.5,142.6 107.5,142.6"/>
      <polygon role="img" aria-label="Photo of solar panel field" fill="url(#spreadPanelTone)"
        points="205,110 170,49.4 100,49.4 65,110 100,170.6 170,170.6"/>
      <polygon fill="var(--tab)"
        points="378,85 335.5,11.4 250.5,11.4 208,85 250.5,158.6 335.5,158.6"/>
    </svg>
    <p class="hex-quote">Amest, mollis a iaculis nec, bibendum vel felis. Pellentesque dictum nisl sed augue gravida molestie, sed pharetra tortor ac scelerisque hendrerit. Etiam vel neque elit.</p>

    <p class="body-text" style="left:20px; top:290px; width:165px;">Curabitur vehicula lorem sem et nisi gravida euismod. Cras vitae accumsan ligula, sagittis vitae nisi sit amet tincidunt. Nulla tincidunt auctor magna, hendrerit eu tellus. Cras malesuada nunc id faucibus mi. Morbi vel tempus eleifend a. Maecenas dignissim ante fermentum. Phasellus aliquet turpis egestas. Pellentesque habitant morbi tristique senectus et netus et malesuada.</p>
    <p class="body-text" style="left:198px; top:290px; width:165px;">Malesuada fames ac turpis egestas. Nulla in pharetra augue. Curabitur dictum tortor ut malesuada pellentesque tempus. Vivamus et nisi aliquam, varius dolor a, ultrices ante. Donec hendrerit quis leo tristique, et varius ipsum luctus. Nam eget accumsan sem. Duis ac pulvinar nisi. Curabitur adipiscing, nunc ut lobortis gravida, mauris nisi consectetur mauris, et placerat magna augue in diam. Sed luctus et neque ut lobortis.</p>

    <svg class="bottom-band" viewBox="0 0 380 40">
      <path d="M40 8 C 160 2, 280 2, 380 6 L 380 14 C 280 10, 160 10, 40 16 Z" fill="var(--brand-green)"/>
    </svg>
    <div class="page-tab" style="left:318px; top:452px;">5</div>
  </section>

  <div class="gutter"></div>

</body>
</html>
```